Payment company requires web design

We need a web design for a new company based in Singapore.

The company focuses on providing 2 key products: 1) an alternative payment option (i.e. like zorbu or plendrixon options) on the traditional checkout process 2) a replacement/outsource of a merchants payment page. Key in the UX flow is a end customer dashboard that manages all payments.

We look to provide a simple, fluid and easy to use payment process. The dashboard is minimalistic that allows easy navigation, review of transactions and all available options through gamification.

The final design should communicate ease of use, flexibility and transparency.

The value is for the merchant - retail/travel/insurance companies. However its the merchant's end customers that are the target and who the UX is built for.

It Company

malvri

5+ page

ec1f27

• 7 pages mimicking UX flow
• payment page * 2 - 1) alternative payment type 2) outsource of merchants payment page to our business
• our landing page
• end customer verification page
• end customer registration
• customer dashboard
• UX flow in attached file
• open to ideas
• have asked for the logo to be added
• logo to have the colour red (chinese for prosperity)
• the company is all about flexibility, transparency in personal finance management with the option of instalment payments

```html
<!DOCTYPE html>
<html lang="en">
<head>
<meta charset="utf-8">
<title>Malvri — Payments made simple</title>
<link rel="stylesheet" href="https://fonts.googleapis.com/css2?family=Nunito+Sans:wght@300;400;600&display=swap">
<style>
  :root {
    --red: #ec1f27;
    --ink: #3d3d3d;
    --muted: #7a7a7a;
    --light: #f2f2f2;
    --row: #e4e4e4;
    --line: #cfcfcf;
    --white: #ffffff;
  }
  * { box-sizing: border-box; margin: 0; padding: 0; }
  html, body { width: 1200px; height: 2236px; overflow: hidden; }
  body { position: relative; background: var(--white); font-family: "Nunito Sans", Arial, sans-serif; color: var(--ink); }
  .abs { position: absolute; }

  /* Header */
  .brand { left: 146px; top: 36px; font-size: 46px; font-weight: 400; color: var(--red); letter-spacing: -0.5px; }
  .nav { left: 417px; top: 50px; width: 470px; height: 26px; font-size: 19px; }
  .nav a { position: absolute; top: 0; color: var(--ink); text-decoration: none; white-space: nowrap; }
  .search-icon { left: 904px; top: 51px; }
  .register { left: 958px; top: 47px; width: 100px; height: 32px; border: 2px solid #8a8a8a; font-size: 15px; color: var(--ink); display: flex; align-items: center; justify-content: center; }

  /* Hero */
  .hero-photo { left: 0; top: 0; width: 1200px; height: 580px; background: linear-gradient(120deg, #e9e6e4 0%, #f4f2f0 40%, #e2dedb 70%, #efedeb 100%); }
  .hero-title { left: 146px; top: 224px; font-size: 41px; font-weight: 400; color: #4a4a4a; letter-spacing: 0.3px; }
  .hero-sub { left: 146px; top: 278px; font-size: 29px; font-weight: 300; color: #4a4a4a; }
  .btn-primary { left: 146px; top: 335px; width: 164px; height: 40px; background: var(--red); color: var(--white); font-size: 18px; display: flex; align-items: center; justify-content: center; }
  .dots { left: 146px; top: 398px; display: flex; gap: 8px; }
  .dots span { width: 14px; height: 14px; border-radius: 50%; background: #b9b9b9; }
  .dots span.on { background: transparent; border: 2px solid #b9b9b9; }
  .device { left: 695px; top: 122px; width: 272px; height: 460px; border-radius: 40px 40px 0 0; background: linear-gradient(180deg, #d9d9dc 0%, #8d8596 30%, #b6b0bf 45%, #2f8fd1 60%, #2a86c9 100%); border: 4px solid #c9c9cc; }

  /* Features band */
  .band { left: 0; top: 0; }
  .feature { width: 330px; text-align: center; color: var(--white); }
  .feature .icon { width: 104px; height: 104px; margin: 0 auto; border: 3px solid var(--white); border-radius: 50%; display: flex; align-items: center; justify-content: center; }
  .feature h3 { font-size: 21px; font-weight: 400; margin-top: 24px; }
  .feature p { font-size: 12px; line-height: 17px; margin: 14px auto 0; width: 250px; }
  .feature .btn-outline { display: inline-block; margin-top: 22px; width: 103px; height: 31px; line-height: 28px; border: 1.5px solid var(--white); font-size: 13px; }

  /* About */
  .section-title { width: 1200px; left: 0; text-align: center; font-size: 33px; font-weight: 400; color: var(--ink); }
  .about-title { top: 962px; display: flex; justify-content: center; align-items: center; gap: 20px; }
  .about-title::before, .about-title::after { content: ""; width: 56px; height: 1px; background: #9a9a9a; }
  .about-text { left: 190px; top: 1024px; width: 820px; text-align: center; font-size: 15.5px; line-height: 27.5px; color: var(--muted); }
  .btn-ghost { left: 526px; top: 1161px; width: 144px; height: 40px; border: 1.5px solid #bdbdbd; color: var(--muted); font-size: 15px; display: flex; align-items: center; justify-content: center; letter-spacing: 0.5px; }

  /* FAQ */
  .faq-bg { left: 0; top: 1259px; width: 1200px; height: 444px; background: var(--light); }
  .faq-title { top: 1287px; }
  .faq { left: 219px; top: 1343px; width: 766px; }
  .faq-q { height: 45px; padding-left: 20px; display: flex; align-items: center; font-size: 17px; background: var(--row); border: 1px solid #d6d6d6; color: var(--ink); margin-bottom: 2px; }
  .faq-q.open { background: var(--red); color: var(--white); border-color: var(--red); margin-bottom: 0; }
  .faq-a { height: 118px; background: var(--white); border: 1px solid #d6d6d6; border-top: 0; padding: 14px 20px; display: flex; gap: 12px; margin-bottom: 2px; }
  .faq-a b { color: var(--red); font-weight: 400; font-size: 16px; }
  .faq-a p { font-size: 12.5px; line-height: 22px; color: #9b9b9b; }

  /* Customer services */
  .service-photo { left: 693px; top: 1703px; width: 507px; height: 364px; background: linear-gradient(135deg, #f2f2f2 0%, #e6e6e6 35%, #3a3a3a 55%, #f1f1f1 65%, #c9a979 85%, #1b1b1b 100%); }
  .service-title { left: 162px; top: 1792px; font-size: 33px; font-weight: 400; color: var(--red); }
  .service-text { left: 162px; top: 1844px; width: 490px; font-size: 14.5px; line-height: 23px; color: var(--muted); }
  .search-field { left: 161px; top: 1932px; width: 360px; height: 38px; border: 1px solid #d3d3d3; border-radius: 19px; background: var(--white); }
  .search-field span { position: absolute; left: 18px; top: 10px; font-size: 13px; color: #aaa; }
  .search-btn { left: 416px; top: 1932px; width: 105px; height: 38px; border-radius: 19px; background: var(--red); color: var(--white); font-size: 17px; display: flex; align-items: center; justify-content: center; }

  /* Footer */
  .footer-rule { left: 0; top: 2067px; width: 1200px; height: 1px; background: #dcdcdc; }
  .footer-nav a { position: absolute; top: 2110px; font-size: 18px; color: var(--ink); text-decoration: none; white-space: nowrap; }
  .copyright { left: 0; width: 1200px; top: 2140px; text-align: center; font-size: 11px; color: #8a8a8a; }
  .social { left: 535px; top: 2175px; display: flex; gap: 3px; }
  .social span { width: 30px; height: 30px; border: 1.5px solid #555; border-radius: 50%; }
</style>
</head>
<body>

<div class="abs hero-photo" role="img" aria-label="Softly faded photo of people paying with a phone and card"></div>
<div class="abs device" role="img" aria-label="Smartphone showing a checkout screen with total and card details"></div>

<svg class="abs band" width="1200" height="900" viewBox="0 0 1200 900" aria-hidden="true">
  <polygon points="0,574 1200,484 1200,899 0,899" fill="#ec1f27"/>
</svg>

<header>
  <div class="abs brand">malvri</div>
  <nav class="abs nav">
    <a style="left:0" href="#">Home</a>
    <a style="left:88px" href="#">About</a>
    <a style="left:177px" href="#">How it work</a>
    <a style="left:312px" href="#">Services</a>
    <a style="left:419px" href="#">FAQ</a>
  </nav>
  <svg class="abs search-icon" width="22" height="22" viewBox="0 0 22 22" aria-label="Search">
    <circle cx="9" cy="9" r="6.5" fill="none" stroke="#8a8a8a" stroke-width="2.5"/>
    <line x1="14" y1="14" x2="20" y2="20" stroke="#8a8a8a" stroke-width="3" stroke-linecap="round"/>
  </svg>
  <div class="abs register">Register</div>
</header>

<section class="hero">
  <h1 class="abs hero-title">Maecenas aliquet velit</h1>
  <h2 class="abs hero-sub">Neque metus malesuada nec</h2>
  <div class="abs btn-primary">Get Started</div>
  <div class="abs dots"><span class="on"></span><span></span><span></span><span></span></div>
</section>

<section class="features">
  <div class="abs feature" style="left:111px;top:590px">
    <div class="icon">
      <svg width="56" height="50" viewBox="0 0 56 50" aria-hidden="true">
        <path d="M4 4h48l4 14H0z" fill="#fff"/>
        <rect x="6" y="22" width="44" height="26" fill="#fff"/>
        <rect x="22" y="30" width="12" height="18" fill="#ec1f27"/>
      </svg>
    </div>
    <h3>Merchant Payment</h3>
    <p>sociosqu ad litora torquent per conubia nostra per inceptos hymenaeos Proin nulla arcu nonummy luctus</p>
    <span class="btn-outline">Read More</span>
  </div>
  <div class="abs feature" style="left:438px;top:590px">
    <div class="icon">
      <svg width="56" height="56" viewBox="0 0 56 56" aria-hidden="true">
        <rect x="6" y="14" width="30" height="24" rx="3" fill="#fff"/>
        <rect x="12" y="6" width="18" height="10" fill="#fff"/>
        <rect x="24" y="26" width="22" height="30" rx="2" transform="rotate(-30 35 41)" fill="#fff"/>
      </svg>
    </div>
    <h3>Outsourced Payment</h3>
    <p>sociosqu ad litora torquent per conubia nostra per inceptos hymenaeos Proin nulla arcu nonummy luctus</p>
    <span class="btn-outline">Read More</span>
  </div>
  <div class="abs feature" style="left:765px;top:590px">
    <div class="icon">
      <svg width="56" height="50" viewBox="0 0 56 50" aria-hidden="true">
        <rect x="14" y="2" width="26" height="16" rx="2" transform="rotate(20 27 10)" fill="#fff"/>
        <rect x="4" y="16" width="48" height="32" rx="4" fill="#fff"/>
        <rect x="36" y="26" width="16" height="12" rx="2" fill="#ec1f27"/>
      </svg>
    </div>
    <h3>Installment Payments</h3>
    <p>sociosqu ad litora torquent per conubia nostra per inceptos hymenaeos Proin nulla arcu nonummy luctus</p>
    <span class="btn-outline">Read More</span>
  </div>
</section>

<section class="about">
  <h2 class="abs section-title about-title">About Malvri</h2>
  <p class="abs about-text">Etiam eleifend metus vitae adipiscing semper mauris ipsum iaculis elit congue gravida elit mi&nbsp; Maecenas aliquet velit vel turpis Mauris neque metus malesuada nec ultricies sit amet porttitor mattis enim In massa libero interdum nec interdum vel blandit sed nulla In ullamcorper est eget tempor cursus neque mi consectetuer mi a ultricies massa est sed nisl Class aptent taciti sociosqu ad litora torquent per conubia nostra per inceptos</p>
  <div class="abs btn-ghost">READ MORE</div>
</section>

<section class="faq-section">
  <div class="abs faq-bg"></div>
  <h2 class="abs section-title faq-title">FAQ</h2>
  <div class="abs faq">
    <div class="faq-q open">Q: Etiam est nunc venenatis in tristique eu imperdiet ac nisl Cum sociis natoque?</div>
    <div class="faq-a"><b>A:</b><p>Maecenas at justo id velit placerat molestie Donec dictum lectus non odio Cras a ante vitae enim iaculis aliquam Mauris nunc quam venenatis nec euismod sit amet egestas placerat est Pellentesque habitant morbi tristique senectus et netus et malesuada fames ac turpis egestas Cras id elit Integer quis urna Ut ante enim</p></div>
    <div class="faq-q">Q: Morbi porta libero ullamcorper nonummy nibh ligula ?</div>
    <div class="faq-q">Q:&nbsp; Pulvinar metus eget consectetuer augue nisi quis lacus Ut ac mi?</div>
    <div class="faq-q">Q: Auis lacus mollis aliquam Curabitur iaculis tempus?</div>
  </div>
</section>

<section class="services">
  <div class="abs service-photo" role="img" aria-label="Desk photo with laptop keyboard, notebook, phone and a cup of coffee"></div>
  <h2 class="abs service-title">Customer Services</h2>
  <p class="abs service-text">Curabitur vel mi sit amet magna malesuada ultrices Ut nisi erat fermentum vel congue id euismod in elit Fusce ultricies orci ac feugiat suscipit leo massa sodales velit et scelerisque mi tortor at</p>
  <div class="abs search-field"><span>Type here</span></div>
  <div class="abs search-btn">Search</div>
</section>

<footer>
  <div class="abs footer-rule"></div>
  <nav class="footer-nav">
    <a style="left:340px" href="#">Home</a>
    <a style="left:422px" href="#">About</a>
    <a style="left:505px" href="#">How it work</a>
    <a style="left:632px" href="#">Services</a>
    <a style="left:731px" href="#">FAQ</a>
    <a style="left:801px" href="#">Contact</a>
  </nav>
  <p class="abs copyright">© 2016 Company Name&nbsp; All right reserved&nbsp; Term of Use</p>
  <div class="abs social" aria-label="Social links"><span></span><span></span><span></span><span></span></div>
</footer>

</body>
</html>
```